Enterprise image desing

The designs are for a fashion store for young men and women.
Updates

Los diseƱos parecen similares

Target Market(s)

Young

Font styles to use
Sans Serif

Colors
ec1f27
ffffff
1b1b1b

Requirements
Must have
• Use clean and modern sources
Nice to have
• n / a
Should not have
• n / a

```html
<!DOCTYPE html>
<html lang="en">
<head>
<meta charset="utf-8">
<title>Velorane Stationery</title>
<link href="https://fonts.googleapis.com/css2?family=Nunito+Sans:wght@400;600;800&family=Tangerine:wght@700&display=swap" rel="stylesheet">
<style>
:root{
  --navy:#1b2a57;
  --red:#d7262e;
  --white:#ffffff;
  --ink:#1b1b1b;
  --stage:#c8c8c8;
  --pale-red:#fbe6e8;
  --pale-grey:#e6e7ec;
}
*{margin:0;padding:0;box-sizing:border-box}
html,body{width:1200px;height:1200px;overflow:hidden}
body{background:var(--stage);font-family:"Nunito Sans",sans-serif;color:var(--ink);position:relative}
.sheet{position:absolute;background:var(--white);box-shadow:2px 3px 4px rgba(0,0,0,.35);overflow:hidden}
.sheet.dark{background:var(--navy)}
.brand{display:flex;align-items:center;font-weight:800;letter-spacing:.5px;color:var(--navy);line-height:1;white-space:nowrap}
.brand .mark{display:inline-block;background:var(--red);margin-right:.25em;width:.8em;height:.8em}
.dark .brand{color:var(--white)}
.dark .brand .mark{background:var(--white)}
.name{font-size:12px;color:var(--navy)}
.role{font-size:9px;color:var(--ink)}
.contact{font-size:10.5px;line-height:1.45;color:var(--ink)}
.contact li{list-style:none;display:flex;align-items:center;gap:4px}
.contact .gap{margin-top:5px}
.ico{width:10px;height:10px;flex:none}
.address{font-size:10.5px;line-height:1.3;margin-top:5px}
.band{position:absolute;left:0;bottom:0;width:100%}
.letter-body{position:absolute;left:38px;top:90px;width:360px;font-size:7.2px;line-height:15.5px}
.letter-body p{margin-bottom:15px}
.letter-body .to{font-weight:800;line-height:15.5px}
.signature{width:95px;height:42px;background:linear-gradient(90deg,#e9e9e9,#f4f4f4);margin:2px 0}
.compliments{position:absolute;right:22px;bottom:20px;font-family:"Tangerine",cursive;font-weight:700;font-size:20px;color:var(--navy)}
</style>
</head>
<body>

<svg width="0" height="0" style="position:absolute">
  <defs>
    <symbol id="i-mobile" viewBox="0 0 10 10"><circle cx="5" cy="5" r="5" fill="#d7262e"/><rect x="3.3" y="2" width="3.4" height="6" rx=".6" fill="#fff"/></symbol>
    <symbol id="i-phone" viewBox="0 0 10 10"><circle cx="5" cy="5" r="5" fill="#d7262e"/><path d="M2.5 4.2c0-1 5-1 5 0v.6H6.3v-.5H3.7v.5H2.5zM3.4 5h3.2l.6 2H2.8z" fill="#fff"/></symbol>
    <symbol id="i-mail" viewBox="0 0 10 10"><circle cx="5" cy="5" r="5" fill="#d7262e"/><rect x="2.4" y="3.2" width="5.2" height="3.6" fill="#fff"/><path d="M2.4 3.2 5 5.3 7.6 3.2" fill="none" stroke="#d7262e" stroke-width=".6"/></symbol>
    <symbol id="i-web" viewBox="0 0 10 10"><circle cx="5" cy="5" r="5" fill="#d7262e"/><circle cx="5" cy="5" r="2.8" fill="none" stroke="#fff" stroke-width=".7"/><path d="M2.2 5h5.6M5 2.2v5.6" stroke="#fff" stroke-width=".6"/></symbol>
  </defs>
</svg>

<!-- Business card front, navy -->
<section class="sheet dark" style="left:62px;top:50px;width:335px;height:191px">
  <div class="brand" style="position:absolute;left:38px;top:76px;font-size:37px"><span class="mark"></span>VELORANE</div>
</section>

<!-- Business card back, vertical divider -->
<section class="sheet" style="left:442px;top:50px;width:335px;height:192px">
  <div style="position:absolute;left:22px;top:19px">
    <div class="name">Martin Keller</div>
    <div class="role">Director</div>
  </div>
  <div class="brand" style="position:absolute;left:22px;top:145px;font-size:18px"><span class="mark"></span>VELORANE</div>
  <div style="position:absolute;left:187px;top:70px;width:2px;height:100px;background:var(--red)"></div>
  <div style="position:absolute;left:200px;top:68px">
    <ul class="contact">
      <li><svg class="ico"><use href="#i-mobile"/></svg>555-210-4837</li>
      <li><svg class="ico"><use href="#i-phone"/></svg>555-672-1190</li>
      <li class="gap"><svg class="ico"><use href="#i-mail"/></svg>hello@velorane.com</li>
      <li><svg class="ico"><use href="#i-web"/></svg>www.velorane.com</li>
    </ul>
    <div class="address">000 Linden Street<br>OR 97204,xxxxxxx</div>
  </div>
</section>

<!-- Business card front, navy alt -->
<section class="sheet dark" style="left:809px;top:53px;width:335px;height:191px">
  <div class="brand" style="position:absolute;left:39px;top:76px;font-size:37px"><span class="mark"></span>VELORANE</div>
</section>

<!-- Business card back, band -->
<section class="sheet" style="left:60px;top:281px;width:335px;height:191px">
  <div style="position:absolute;left:22px;top:27px;display:flex;align-items:center;gap:5px">
    <span class="name">Martin Keller</span>
    <span style="width:1px;height:11px;background:var(--navy)"></span>
    <span class="role">Director</span>
  </div>
  <div class="brand" style="position:absolute;left:202px;top:26px;font-size:17px"><span class="mark"></span>VELORANE</div>
  <div style="position:absolute;left:22px;top:70px">
    <ul class="contact">
      <li><svg class="ico"><use href="#i-mobile"/></svg>555-210-4837</li>
      <li><svg class="ico"><use href="#i-phone"/></svg>555-672-1190</li>
      <li class="gap"><svg class="ico"><use href="#i-mail"/></svg>hello@velorane.com</li>
      <li><svg class="ico"><use href="#i-web"/></svg>www.velorane.com</li>
    </ul>
    <div class="address">000 Linden Street<br>OR 97204,xxxxxxx</div>
  </div>
  <svg class="band" viewBox="0 0 335 19" height="19" preserveAspectRatio="none">
    <polygon points="0,0 209,0 221,19 0,19" fill="#1b2a57"/>
    <polygon points="216,0 335,0 335,19 228,19" fill="#d7262e"/>
  </svg>
</section>

<!-- Business card back, corner block -->
<section class="sheet" style="left:440px;top:270px;width:335px;height:192px">
  <div style="position:absolute;left:30px;top:25px">
    <div class="name" style="color:var(--red)">Martin Keller</div>
    <div class="role">Director</div>
  </div>
  <div style="position:absolute;left:30px;top:72px">
    <ul class="contact">
      <li><svg class="ico"><use href="#i-mobile"/></svg>555-210-4837</li>
      <li><svg class="ico"><use href="#i-phone"/></svg>555-672-1190</li>
      <li class="gap"><svg class="ico"><use href="#i-mail"/></svg>hello@velorane.com</li>
      <li><svg class="ico"><use href="#i-web"/></svg>www.velorane.com</li>
    </ul>
    <div class="address">000 Linden Street<br>OR 97204,xxxxxxx</div>
  </div>
  <div style="position:absolute;left:212px;top:68px;width:123px;height:124px;background:var(--red)"></div>
</section>

<!-- Business card front, white -->
<section class="sheet" style="left:810px;top:271px;width:335px;height:191px">
  <div class="brand" style="position:absolute;left:39px;top:76px;font-size:37px"><span class="mark"></span>VELORANE</div>
</section>

<!-- Letterhead -->
<section class="sheet" style="left:114px;top:518px;width:437px;height:619px">
  <div class="brand" style="position:absolute;left:148px;top:26px;font-size:21px"><span class="mark"></span>VELORANE</div>
  <div class="letter-body">
    <p class="to">To<br>Lorem Ipsum is simply<br>Lorem Ipsum is Lorem Ipsum is<br>Lorem Ipsum is</p>
    <p>dummy text of the printing and typesetting industry. Lorem Ipsum has been the industry's standard dummy text ever since the 1500s, when an unknown printer took a galley of type and scrambled it to make a type specimen book. It has survived not only five centuries, but also the leap into electronic typesetting, remaining essentially unchanged.</p>
    <p>It is a long established fact that a reader will be distracted by the readable content of a page when looking at its layout. The point of using Lorem Ipsum is that it has a more-or-less normal distribution of letters, as opposed to using 'Content here, content here', making it look like readable English. Many desktop publishing packages and web page editors now use Lorem Ipsum as their default model text, and a search for 'lorem .</p>
    <p>Contrary to popular belief, Lorem Ipsum is not simply random text. It has roots in a piece of classical Latin literature from 45 BC, making it over 2000 years old. Daniel Ortwin, a Latin professor at Ashford College in Vermont, looked up one of the more obscure Latin words, consectetur, from a Lorem Ipsum passage,</p>
    <div>Lorem Ipsum</div>
    <div class="signature" role="img" aria-label="Handwritten signature"></div>
    <div>Lorem Ipsum is a dummy</div>
  </div>
  <svg class="band" viewBox="0 0 437 25" height="25" preserveAspectRatio="none">
    <polygon points="0,0 270,0 285,25 0,25" fill="#1b2a57"/>
    <polygon points="278,0 437,0 437,25 293,25" fill="#d7262e"/>
  </svg>
</section>

<!-- Envelope front -->
<section class="sheet" style="left:580px;top:523px;width:460px;height:189px">
  <div class="brand" style="position:absolute;left:14px;top:12px;font-size:12px"><span class="mark"></span>VELORANE</div>
  <div style="position:absolute;left:14px;top:29px;font-size:7px;line-height:9.5px;color:#555">000 Linden Street<br>OR 97204,xxxxxxx</div>
  <div style="position:absolute;left:348px;top:76px;width:112px;height:113px;background:var(--pale-red)"></div>
</section>

<!-- Envelope back -->
<section class="sheet" style="left:580px;top:726px;width:462px;height:189px">
  <svg style="position:absolute;left:0;top:0" width="462" height="75" viewBox="0 0 462 75">
    <path d="M1 1 L28 65 Q31 72 40 72 L422 72 Q431 72 434 65 L461 1" fill="none" stroke="#9a9a9a" stroke-width="1"/>
  </svg>
</section>

<!-- Compliment slip -->
<section class="sheet" style="left:590px;top:962px;width:385px;height:175px">
  <div class="brand" style="position:absolute;left:12px;top:15px;font-size:11px"><span class="mark"></span>VELORANE</div>
  <div class="compliments" style="bottom:22px">With Compliments</div>
  <svg class="band" viewBox="0 0 385 13" height="13" preserveAspectRatio="none">
    <polygon points="0,0 242,0 250,13 0,13" fill="#1b2a57"/>
    <polygon points="246,0 385,0 385,13 254,13" fill="#d7262e"/>
  </svg>
</section>

</body>
</html>
```